Quorvex clinic business card - double sided for young clinic

I require business cards for my aesthetic clinic specialising in the below treatments. I would like the cards to be modern as my clinic base are young 22-35 years old. I require my logo on it and would like the edges to be rounded.

I have an aesthetic clinic specialising in :
Quorvex
Lip Enhancement
Chemical Peels
Facial Fillers
Non Surgical Face Lift

I would the cards to have the following information on them:
My logo - (in grey/silver)
address
Phone number
services

Colours :
White/grey/silver and red

a nice image on there, perhaps a set of lips as this is a main service i deliver

Company Name: PDA Address: 52 Farrowmere Road, 4 Brackwell High Street, KT9 4WQ Phone: 0208 794 2160 Website: www.penningtondoweaesthetics.co.uk

Target Market(s)

clinics 22-45 years old mainly female

Industry/Entity Type

Business

Contact Information for Business Card

as above

Requirements
Must have
• logo
• Address
• Email
• Phone number
• Services i offer
Nice to have
• images

```html
<!DOCTYPE html>
<html lang="en">
<head>
<meta charset="utf-8">
<title>PDA Business Card</title>
<link href="https://fonts.googleapis.com/css2?family=Mulish:wght@400;700&display=swap" rel="stylesheet">
<style>
  :root {
    --backdrop: #1b1b1b;
    --card: #141414;
    --silver: #c9c9c9;
    --grey: #a8a8a8;
    --rule: #4a4a4a;
  }
  * { margin: 0; padding: 0; box-sizing: border-box; }
  html, body { width: 1200px; height: 923px; overflow: hidden; }
  body {
    background: var(--backdrop);
    font-family: "Mulish", sans-serif;
    color: var(--silver);
    position: relative;
  }
  .card {
    position: absolute;
    left: 290px;
    width: 620px;
    height: 401px;
    background: var(--card);
    border-radius: 22px;
    box-shadow: 0 10px 30px rgba(0,0,0,.55);
  }
  .card--back { top: 40px; }
  .card--front { top: 482px; }

  /* back side */
  .services {
    position: absolute;
    left: 60px; top: 70px;
    width: 230px;
    text-align: center;
    font-size: 17px;
    line-height: 1.55;
    color: var(--grey);
    list-style: none;
  }
  .services__title { font-weight: 700; color: var(--silver); margin-bottom: 2px; }
  .brand-mark {
    position: absolute;
    display: flex; align-items: center; gap: 14px;
    color: var(--silver);
  }
  .brand-mark__dot {
    border-radius: 50%;
    background: var(--silver);
  }
  .card--back .brand-mark { right: 70px; top: 170px; font-size: 48px; letter-spacing: 4px; }
  .card--back .brand-mark__dot { width: 40px; height: 40px; }

  /* front side */
  .identity {
    position: absolute;
    left: 40px; top: 110px;
    width: 240px;
    display: flex; flex-direction: column; align-items: center;
  }
  .identity .brand-mark { position: static; font-size: 34px; letter-spacing: 3px; gap: 10px; }
  .identity .brand-mark__dot { width: 26px; height: 26px; }
  .identity__name {
    margin-top: 18px;
    text-align: center;
    font-size: 19px;
    letter-spacing: 3px;
    line-height: 1.3;
    text-transform: uppercase;
    color: var(--silver);
  }
  .divider {
    position: absolute;
    left: 300px; top: 90px;
    width: 1px; height: 230px;
    background: var(--rule);
  }
  .contact {
    position: absolute;
    left: 328px; top: 82px;
    font-size: 16px;
    line-height: 1.45;
    color: var(--grey);
  }
  .contact__name { font-weight: 700; font-size: 19px; color: var(--silver); }
  .contact__role { margin-bottom: 14px; }
  .contact__address { margin-bottom: 14px; }
  .contact__line { display: flex; align-items: center; gap: 8px; font-size: 15px; }
  .contact__line svg { width: 15px; height: 15px; flex: none; }
</style>
</head>
<body>
  <section class="card card--back">
    <ul class="services">
      <li class="services__title">Specialising in :</li>
      <li>Quorvex</li>
      <li>Lip Enhancement</li>
      <li>Chemical Peels</li>
      <li>Facial Fillers</li>
      <li>Non Surgical Face Lift</li>
    </ul>
    <div class="brand-mark"><span class="brand-mark__dot"></span><span>PDA</span></div>
  </section>

  <section class="card card--front">
    <div class="identity">
      <div class="brand-mark"><span class="brand-mark__dot"></span><span>PDA</span></div>
      <p class="identity__name">Pennington Dowe<br>Aesthetics</p>
    </div>
    <span class="divider"></span>
    <div class="contact">
      <p class="contact__name">Petra Dowe</p>
      <p class="contact__role">Aesthetician</p>
      <p class="contact__address">52 Farrowmere Road<br>4 Brackwell High Street, KT9 4WQ</p>
      <p class="contact__line">
        <svg viewBox="0 0 16 16" fill="none" stroke="currentColor" stroke-width="1.3"><path d="M3 2h3l1 3-2 1.5a9 9 0 0 0 4.5 4.5L11 9l3 1v3a1 1 0 0 1-1 1A12 12 0 0 1 2 3a1 1 0 0 1 1-1z"/></svg>
        0208 794 2160
      </p>
      <p class="contact__line">
        <svg viewBox="0 0 16 16" fill="none" stroke="currentColor" stroke-width="1.3"><rect x="1.5" y="3.5" width="13" height="9"/><path d="M1.5 3.5 8 9l6.5-5.5"/></svg>
        pdabrackwellbookings@mailbox.com
      </p>
      <p class="contact__line">
        <svg viewBox="0 0 16 16" fill="none" stroke="currentColor" stroke-width="1.3"><circle cx="8" cy="8" r="6.5"/><path d="M1.5 8h13M8 1.5c-3 3.5-3 9.5 0 13M8 1.5c3 3.5 3 9.5 0 13"/></svg>
        www.penningtondoweaesthetics.co.uk
      </p>
    </div>
  </section>
</body>
</html>
```